Brantley Studios photography and video creator

I need a business card for my production company. I shoot photography and videography for real estate, adventure sports and businesses

Contact Information for Business Card

simple not to busy

Colors

Designer to choose colors to be used in the design.

Requirements
Must have
• derek@brantleystudios.ca
• phone -5873304127
• instagram derek_brantley

```html
<!DOCTYPE html>
<html lang="en">
<head>
<meta charset="utf-8">
<title>Brantley Studios — Business Card</title>
<link href="https://fonts.googleapis.com/css2?family=Montserrat:wght@300;600&family=Pinyon+Script&display=swap" rel="stylesheet">
<style>
  :root {
    --page-bg: #e4e5e8;
    --card-light: #f7f7f7;
    --card-mid: #dcdcdc;
    --ink: #1b1b1b;
    --ink-soft: #2a2a2a;
    --band: #111111;
    --white: #ffffff;
    --mist: #c9c9c9;
  }
  * { margin: 0; padding: 0; box-sizing: border-box; }
  html, body {
    width: 1200px; height: 1200px; overflow: hidden;
    background: var(--page-bg);
    font-family: "Montserrat", sans-serif;
  }
  .card {
    position: absolute; left: 274px; width: 658px; height: 384px;
    background: linear-gradient(100deg, var(--card-mid) 0%, var(--card-light) 45%, var(--card-mid) 100%);
    overflow: hidden;
  }
  .card--front { top: 144px; }
  .card--back { top: 652px; }

  .brand {
    position: absolute; display: flex; align-items: center; gap: 16px;
    left: 50%; transform: translateX(-50%);
    white-space: nowrap;
  }
  .card--front .brand { top: 176px; }
  .card--back .brand { top: 118px; }
  .brand__dot {
    width: 34px; height: 34px; border-radius: 50%; background: var(--ink);
    flex: none;
  }
  .card--back .brand__dot { width: 28px; height: 28px; }
  .brand__name {
    font-weight: 600; color: var(--ink); letter-spacing: 2px;
    font-size: 34px; text-transform: uppercase;
  }
  .card--back .brand__name { font-size: 28px; }

  .backdrop-scene {
    position: absolute; inset: 0;
    background: radial-gradient(ellipse at 75% 35%, var(--mist) 0%, rgba(201,201,201,0) 60%),
                linear-gradient(180deg, rgba(255,255,255,0) 40%, rgba(190,190,190,0.5) 85%);
  }

  .name-band {
    position: absolute; left: 0; right: 0; top: 266px; height: 36px;
    background: var(--band);
    display: flex; align-items: center; justify-content: center;
  }
  .name-band__text {
    font-family: "Pinyon Script", cursive;
    color: var(--white); font-size: 30px; line-height: 1;
  }

  .contacts {
    position: absolute; left: 28px; right: 36px; top: 326px;
    display: flex; justify-content: space-between; align-items: center;
    font-weight: 300; font-size: 16px; color: var(--ink-soft);
  }
  .contact { display: flex; align-items: center; gap: 5px; }
  .contact svg { flex: none; }
  .contact__square {
    width: 14px; height: 14px; background: var(--ink-soft); border-radius: 2px; flex: none;
  }
</style>
</head>
<body>
  <section class="card card--front">
    <div class="brand">
      <span class="brand__dot"></span>
      <span class="brand__name">Brantley Studios</span>
    </div>
  </section>

  <section class="card card--back">
    <div class="backdrop-scene" role="img" aria-label="Faint misty landscape of mountains and a tall pine tree"></div>
    <div class="brand">
      <span class="brand__dot"></span>
      <span class="brand__name">Brantley Studios</span>
    </div>
    <div class="name-band">
      <span class="name-band__text">Derek Brantley</span>
    </div>
    <div class="contacts">
      <span class="contact">
        <svg width="12" height="20" viewBox="0 0 12 20" aria-hidden="true">
          <rect x="1" y="1" width="10" height="18" rx="2" fill="none" stroke="#2a2a2a" stroke-width="1.6"/>
          <line x1="4.5" y1="16" x2="7.5" y2="16" stroke="#2a2a2a" stroke-width="1.4"/>
        </svg>
        5873304127
      </span>
      <span class="contact">
        <svg width="20" height="14" viewBox="0 0 20 14" aria-hidden="true">
          <rect x="0.5" y="0.5" width="19" height="13" fill="#2a2a2a"/>
          <polyline points="1,1 10,8 19,1" fill="none" stroke="#f2f2f2" stroke-width="1.4"/>
        </svg>
        derek@brantleystudios.ca
      </span>
      <span class="contact">
        <span class="contact__square"></span>
        derek_brantley
      </span>
    </div>
  </section>
</body>
</html>
```